Polystyrene Environmental Synopsis

We need a fact sheet for quick reference that groups information units and has a simple but engaging visual presentation of the text and various infographics. We are a trade association representing polystyrene foam manufacturers and this piece is intended to help our members provide effective messaging to their sales personnel.

To view our typical company design/style please see our website at www.foamtradeunion.org. Our primary RGB colors are: (187,140,9); (94,47,29); (94,138,164); and (164,167,15). Secondary RGB colors are (249,162,28) and (218,210,208). Our title/header font is DIN Next LT Pro and our copy font is Calibri 10.5 pt. We can deviate from the font specification if beneficial.

Target Market(s)

Polystyrene manufacturer plant workers and other employees.

Font styles to use
Sans Serif

Requirements
Must have
• Information presentation must be clean and easy to reference.

```html
<!DOCTYPE html>
<html lang="en">
<head>
<meta charset="utf-8">
<title>EPS Talking Points</title>
<link rel="stylesheet" href="https://fonts.googleapis.com/css2?family=Mulish:wght@600;700;800&display=swap">
<style>
  :root {
    --brown: #4a1d16;
    --green: #8aa800;
    --tan: #dfba8a;
    --cup-light: #ffffff;
    --cup-shade: #e4e9e6;
  }
  html, body { margin: 0; padding: 0; overflow: hidden; }
  body { width: 1200px; height: 1033px; background: var(--brown); }
  .sheet {
    position: relative; width: 1200px; height: 1033px; overflow: hidden;
    background: var(--brown); font-family: "Mulish", Arial, sans-serif;
  }
  .title-band {
    position: absolute; left: 0; top: 32px; width: 1200px; height: 104px;
    background: var(--green);
  }
  .title {
    position: absolute; left: 196px; top: 43px; margin: 0; white-space: nowrap;
    font-size: 78px; font-weight: 800; color: var(--brown); letter-spacing: -1.5px; line-height: 1;
  }
  .intro {
    position: absolute; left: 58px; top: 178px; margin: 0; white-space: nowrap;
    font-size: 25px; font-weight: 700; line-height: 43px; color: var(--green); letter-spacing: 0.9px;
  }
  .section-banner { position: absolute; left: 0; top: 470px; }
  .section-title {
    position: absolute; left: 70px; top: 493px; margin: 0;
    font-size: 56px; font-weight: 800; color: var(--brown); line-height: 1; letter-spacing: -0.8px;
  }
  .recycle-icon { position: absolute; left: 32px; top: 637px; }
  .points { position: absolute; left: 0; top: 0; margin: 0; padding: 0; list-style: none; }
  .point {
    position: absolute; font-size: 39px; font-weight: 700; color: var(--green);
    line-height: 47px; white-space: nowrap; letter-spacing: 0.3px;
  }
  .cup-art {
    position: absolute; left: 886px; top: 186px; width: 314px; height: 806px;
    background: linear-gradient(90deg, var(--cup-shade) 0%, var(--cup-light) 65%, var(--cup-shade) 100%);
  }
</style>
</head>
<body>
<main class="sheet">
  <div class="title-band"></div>
  <h1 class="title">EPS TALKING POINTS</h1>

  <p class="intro">Polystyrene bans, recycling, and human health are top<br>objections facing the EPS industry. When confronted<br>with false allegations about EPS, here are some fast<br>facts to help respond proactively. Perfect for packaging<br>conferences, social media, and sales objectives.</p>

  <svg class="section-banner" width="540" height="105" viewBox="0 0 540 105">
    <polygon points="0,0 538,0 495,104 0,104" fill="var(--green)"/>
  </svg>
  <h2 class="section-title">RECYCLING</h2>

  <svg class="recycle-icon" width="140" height="135" viewBox="-70 -70 140 135" aria-hidden="true">
    <defs>
      <g id="chase-arrow">
        <path d="M10 -9 L60 -9 L60 -21 L92 0 L60 21 L60 9 L10 9 Z"
              fill="var(--tan)" stroke="var(--tan)" stroke-width="4" stroke-linejoin="round"/>
      </g>
    </defs>
    <g transform="translate(0 -62) rotate(60)"><use href="#chase-arrow"/></g>
    <g transform="rotate(120) translate(0 -62) rotate(60)"><use href="#chase-arrow"/></g>
    <g transform="rotate(240) translate(0 -62) rotate(60)"><use href="#chase-arrow"/></g>
  </svg>

  <ul class="points">
    <li class="point" style="left:245px; top:630px;">EPS is Recyclable</li>
    <li class="point" style="left:238px; top:714px;">New EPS Recycling<br>Technologies Are Emerging</li>
    <li class="point" style="left:238px; top:852px;">EPS End-Markets Show<br>Consistent Growth</li>
  </ul>

  <div class="cup-art" role="img" aria-label="Illustration of a white foam cup filled with coffee"></div>
</main>
</body>
</html>
```